Business cards for education company

We need a business card design for a relatively new company based in Queensland and operating across Australia. We resell diploma level education courses which include Business, Management, Finance, Community Services & Government courses. We offer over 20 different courses.
The target market is for anyone 16 years of age and older. There is no age limit.

We would like to see the design use the color blue and silver. The final design should communicate professionalism and a bright future.

We sell education but are also promoting the career they see themselves in 2-3 years in the future

Our company logo is attached.

Target Market(s)

We target all age groups above 16 years of age. The main target market would be people aged between 17-35.

We focus on those people who cannot make it into University or do not want to commit the time to a full degree.

Industry/Entity Type

Education

Requirements
Must have
• Professional
Company logo
website
Contact details:

Please use the following example:

Lionel Parfitt
Senior Education Consultant
0417 386 591
Lionel.parfitt@brightwaylearninghub.com.au
www.brightwaylearninghub.com.au

```html
<!DOCTYPE html>
<html lang="en">
<head>
<meta charset="utf-8">
<title>Brightway Learning Hub — Business Card</title>
<link rel="stylesheet" href="https://fonts.googleapis.com/css2?family=Libre+Baskerville:wght@400;700&family=Open+Sans:wght@400&display=swap">
<style>
  :root {
    --page: #ffffff;
    --frame: #8a8a8a;
    --card: #f4f4f4;
    --brand-blue: #2f86e0;
    --brand-navy: #1d4f98;
    --ink-grey: #505050;
    --band: #111111;
    --band-divider: #9a9a9a;
  }
  * { margin: 0; padding: 0; box-sizing: border-box; }
  html, body {
    width: 1200px;
    height: 698px;
    overflow: hidden;
    background: var(--page);
  }
  .card-sheet {
    position: relative;
    width: 1200px;
    height: 698px;
    border: 1px solid var(--frame);
    background: var(--page);
  }
  .card-face {
    position: absolute;
    left: 35px;
    top: 31px;
    width: 1138px;
    height: 636px;
    background: var(--card);
  }
  .brand {
    position: absolute;
    left: 34px;
    top: 52px;
    display: flex;
    align-items: center;
    gap: 18px;
  }
  .brand-dot {
    width: 62px;
    height: 62px;
    border-radius: 50%;
    background: var(--brand-blue);
  }
  .brand-name {
    font-family: "Libre Baskerville", Georgia, serif;
    font-weight: 700;
    font-size: 30px;
    line-height: 1.1;
    color: var(--brand-navy);
    text-transform: uppercase;
  }
  .phone {
    position: absolute;
    right: 32px;
    top: 42px;
    font-family: "Libre Baskerville", Georgia, serif;
    font-weight: 700;
    font-size: 30px;
    color: var(--brand-blue);
  }
  .identity {
    position: absolute;
    left: 0;
    right: 0;
    top: 258px;
    text-align: center;
    transform: translateX(-35px);
  }
  .person-name {
    font-family: "Libre Baskerville", Georgia, serif;
    font-weight: 700;
    font-size: 72px;
    letter-spacing: 1px;
    line-height: 1;
    color: var(--brand-blue);
    text-transform: uppercase;
  }
  .person-role {
    margin-top: 22px;
    font-family: "Libre Baskerville", Georgia, serif;
    font-weight: 400;
    font-size: 36px;
    color: var(--ink-grey);
  }
  .contact-band {
    position: absolute;
    left: 0;
    bottom: 0;
    width: 100%;
    height: 100px;
    background: var(--band);
    display: flex;
    align-items: center;
    justify-content: center;
    gap: 18px;
    font-family: "Open Sans", Arial, sans-serif;
    font-size: 23px;
    color: var(--brand-blue);
  }
  .band-divider {
    width: 1px;
    height: 30px;
    background: var(--band-divider);
  }
</style>
</head>
<body>
  <div class="card-sheet">
    <div class="card-face">
      <div class="brand">
        <div class="brand-dot"></div>
        <div class="brand-name">Brightway<br>Learning Hub</div>
      </div>

      <div class="phone">Tel - 0417 386 591</div>

      <div class="identity">
        <h1 class="person-name">Lionel Parfitt</h1>
        <p class="person-role">Senior Education Consultant</p>
      </div>

      <div class="contact-band">
        <span class="website">www.brightwaylearninghub.com.au</span>
        <span class="band-divider"></span>
        <span class="email">Lionel.parfitt@brightwaylearninghub.com.au</span>
      </div>
    </div>
  </div>
</body>
</html>
```